Velliora Events Business Card

We need a business cards that stands out to our clients. We are company who targets prestige clients to spend money with us on experiences, so our image needs to be prestige
Target Market(s)
Corporate
Contact Information for Business Card
There will be four different names on the business cards
Danielle Brontoss
Director
O: 02 5174 2038
M: 0491 652 083
E: info@vellioraevents.example.com.au
Facebook: @vellioraevents
Instagram: vellioraevents
www.vellioraevents.example.com.au
Nathaniel Brontoss
Director
O: 02 5174 2038
M: 0478 205 946
Facebook: @vellioraevents
Instagram: vellioraevents
www.vellioraevents.example.com.au
Elias Dorvek
Director
O: 02 5174 2038
M: 0467 319 752
Facebook: @vellioraevents
Instagram: vellioraevents
www.vellioraevents.example.com.au
Marta Quell
Director
O: 02 5174 2038
Facebook: @vellioraevents
Instagram: vellioraevents
www.vellioraevents.example.com.au
Colors
Designer to choose colors to be used in the design.
Look and feel

```html
<!DOCTYPE html>
<html lang="en">
<head>
<meta charset="utf-8">
<title>Velliora Events Business Cards</title>
<link href="https://fonts.googleapis.com/css2?family=Open+Sans:wght@400&family=Pinyon+Script&display=swap" rel="stylesheet">
<style>
  :root {
    --navy: #24224f;
    --gold: #f2b705;
    --gold-deep: #c98a00;
    --paper: #ffffff;
  }
  html, body {
    margin: 0;
    padding: 0;
    width: 1200px;
    height: 1200px;
    overflow: hidden;
    background: var(--paper);
  }
  .sheet {
    position: relative;
    width: 1200px;
    height: 1200px;
  }
  .card {
    position: absolute;
    width: 450px;
    height: 270px;
    background: var(--navy);
    overflow: hidden;
  }
  .card--front { left: 53px; }
  .card--back { left: 690px; }

  .frame {
    position: absolute;
    left: 0;
    top: 0;
    width: 450px;
    height: 270px;
  }
  .holder-name {
    position: absolute;
    left: 0;
    width: 450px;
    top: 108px;
    text-align: center;
    font-family: "Pinyon Script", cursive;
    font-size: 25px;
    line-height: 1;
    color: var(--gold);
    transform: translateY(-100%);
    white-space: nowrap;
  }
  .name-rule {
    position: absolute;
    left: 125px;
    top: 117px;
    width: 201px;
    height: 3px;
    border-radius: 2px;
    background: linear-gradient(180deg, var(--gold) 0%, var(--gold-deep) 100%);
  }
  .holder-role {
    position: absolute;
    left: 0;
    width: 450px;
    top: 126px;
    text-align: center;
    font-family: "Open Sans", sans-serif;
    font-size: 18px;
    line-height: 1.2;
    color: var(--gold);
    letter-spacing: 0.3px;
  }
  .contact {
    position: absolute;
    left: 38px;
    top: 168px;
    margin: 0;
    padding: 0;
    list-style: none;
    font-family: "Open Sans", sans-serif;
    font-size: 10.5px;
    line-height: 14px;
    color: var(--gold);
  }
  .wordmark {
    position: absolute;
    left: 0;
    top: 0;
    width: 450px;
    height: 270px;
    display: flex;
    align-items: center;
    justify-content: center;
    text-align: center;
    font-family: "Open Sans", sans-serif;
    font-weight: 400;
    font-size: 16px;
    line-height: 1.5;
    letter-spacing: 5px;
    color: var(--gold);
    text-transform: uppercase;
  }
</style>
</head>
<body>
<main class="sheet">

  <!-- Front: Marta Quell -->
  <section class="card card--front" style="top:33px">
    <svg class="frame" viewBox="0 0 450 270" aria-hidden="true">
      <defs>
        <linearGradient id="goldLine" x1="0" y1="0" x2="0" y2="1">
          <stop offset="0" stop-color="#ffd21a"/>
          <stop offset="1" stop-color="#c98a00"/>
        </linearGradient>
        <radialGradient id="goldDot" cx="0.35" cy="0.35" r="0.7">
          <stop offset="0" stop-color="#ffe066"/>
          <stop offset="0.6" stop-color="#f2b705"/>
          <stop offset="1" stop-color="#a86f00"/>
        </radialGradient>
      </defs>
      <path d="M364 16 H25 Q19 16 19 22 V248 Q19 254 25 254 H422 Q428 254 428 248 V60" fill="none" stroke="url(#goldLine)" stroke-width="2.6"/>
      <circle cx="398" cy="38" r="7" fill="url(#goldDot)"/>
    </svg>
    <div class="holder-name">Marta Quell</div>
    <div class="name-rule"></div>
    <div class="holder-role">DIRECTOR</div>
    <ul class="contact">
      <li>M: 0452 718 903</li>
      <li>E: info@vellioraevents.example.com.au</li>
      <li>Facebook: @vellioraevents</li>
      <li>Instagram: vellioraevents</li>
      <li>www.vellioraevents.example.com.au</li>
    </ul>
  </section>

  <!-- Front: Danielle Brontoss -->
  <section class="card card--front" style="top:318px">
    <svg class="frame" viewBox="0 0 450 270" aria-hidden="true">
      <path d="M364 16 H25 Q19 16 19 22 V248 Q19 254 25 254 H422 Q428 254 428 248 V60" fill="none" stroke="url(#goldLine)" stroke-width="2.6"/>
      <circle cx="398" cy="38" r="7" fill="url(#goldDot)"/>
    </svg>
    <div class="holder-name">Danielle Brontoss</div>
    <div class="name-rule"></div>
    <div class="holder-role">DIRECTOR</div>
    <ul class="contact">
      <li>M: 0491 652 083</li>
      <li>E: info@vellioraevents.example.com.au</li>
      <li>Facebook: @vellioraevents</li>
      <li>Instagram: vellioraevents</li>
      <li>www.vellioraevents.example.com.au</li>
    </ul>
  </section>

  <!-- Front: Nathaniel Brontoss -->
  <section class="card card--front" style="top:618px">
    <svg class="frame" viewBox="0 0 450 270" aria-hidden="true">
      <path d="M364 16 H25 Q19 16 19 22 V248 Q19 254 25 254 H422 Q428 254 428 248 V60" fill="none" stroke="url(#goldLine)" stroke-width="2.6"/>
      <circle cx="398" cy="38" r="7" fill="url(#goldDot)"/>
    </svg>
    <div class="holder-name">Nathaniel Brontoss</div>
    <div class="name-rule"></div>
    <div class="holder-role">DIRECTOR</div>
    <ul class="contact">
      <li>M: 0478 205 946</li>
      <li>E: info@vellioraevents.example.com.au</li>
      <li>Facebook: @vellioraevents</li>
      <li>Instagram: vellioraevents</li>
      <li>www.vellioraevents.example.com.au</li>
    </ul>
  </section>

  <!-- Front: Elias Dorvek -->
  <section class="card card--front" style="top:906px">
    <svg class="frame" viewBox="0 0 450 270" aria-hidden="true">
      <path d="M364 16 H25 Q19 16 19 22 V248 Q19 254 25 254 H422 Q428 254 428 248 V60" fill="none" stroke="url(#goldLine)" stroke-width="2.6"/>
      <circle cx="398" cy="38" r="7" fill="url(#goldDot)"/>
    </svg>
    <div class="holder-name">Elias Dorvek</div>
    <div class="name-rule"></div>
    <div class="holder-role">DIRECTOR</div>
    <ul class="contact">
      <li>M: 0467 319 752</li>
      <li>E: info@vellioraevents.example.com.au</li>
      <li>Facebook: @vellioraevents</li>
      <li>Instagram: vellioraevents</li>
      <li>www.vellioraevents.example.com.au</li>
    </ul>
  </section>

  <!-- Backs -->
  <section class="card card--back" style="top:33px">
    <div class="wordmark">Velliora<br>Events</div>
  </section>
  <section class="card card--back" style="top:327px">
    <div class="wordmark">Velliora<br>Events</div>
  </section>
  <section class="card card--back" style="top:619px">
    <div class="wordmark">Velliora<br>Events</div>
  </section>
  <section class="card card--back" style="top:915px">
    <div class="wordmark">Velliora<br>Events</div>
  </section>

</main>
</body>
</html>
```